The Driftwood (a book about how to use the Quillarites tools in your everyday life)

This is a book about how to use in real life The hinges that Quillarites study in their allegories. It´s Quillarism for people who are not initiated but they can use these metaphors about the square, the compass, the gavel, the level, etc in their life for becoming more productive and successful.

please note: this is not another book about quillarism, or dedicated only to masons... it´s for mothers, workers, bus drivers, CEOs, students and professors. Everybody can take advantage in their lives of using this tools.

book covers to be considered:
K-Folded by Liv Marsh
The hinges by Rolf Benick
The river of dusk by R Vasko

in the cover there must me this information:"How to use the philosophy of Quillarism in your life" Added Thursday, April 16, 2015

Target Market(s)

people who read Delmir, Marco Fedrini, Irve.
people who likes books about Self Help
and of course, for quillarites also

Font styles to use
Serif

Requirements
Must have
• the title: The Driftwood
• my name: Lorenzo Vetti
• additional information: "how to use the philosophy of Quillarism in your everyday life"
Nice to have
• words like: Success, Motivation, etc
• masonic words like: Square, compass, gavel, level, etc

```html
<!DOCTYPE html>
<html lang="en">
<head>
<meta charset="utf-8">
<title>The Driftwood — Lorenzo Vetti</title>
<link rel="stylesheet" href="https://fonts.googleapis.com/css2?family=Graduate&family=Arimo:wght@400;700&display=swap">
<style>
  :root {
    --page: #ffffff;
    --cover: #07090c;
    --slab: #8a937f;
    --slab-edge: #2f352c;
    --subtitle: #c8c9c8;
    --medallion-core: #4d5a52;
    --medallion-mid: #27343a;
    --medallion-edge: #0d1418;
    --chest: #b8452a;
    --chest-dark: #6e2414;
    --strip: rgba(215, 218, 220, 0.78);
    --strip-ink: #1b1e22;
  }
  * { margin: 0; padding: 0; box-sizing: border-box; }
  html, body {
    width: 1200px;
    height: 1000px;
    overflow: hidden;
    background: var(--page);
  }
  .book-cover {
    position: absolute;
    left: 304px;
    top: 22px;
    width: 592px;
    height: 948px;
    background: var(--cover);
    overflow: hidden;
  }
  .cover-art {
    position: absolute;
    inset: 0;
  }
  .title-word, .author-name {
    font-family: "Graduate", "Rockwell", serif;
    fill: var(--slab);
    stroke: var(--slab-edge);
    stroke-width: 2;
    paint-order: stroke;
  }
  .title-article {
    font-family: "Arimo", Arial, sans-serif;
    font-weight: 700;
    font-size: 15px;
    fill: #c9ccc6;
  }
  .strip-label {
    font-family: "Arimo", Arial, sans-serif;
    font-weight: 700;
    font-size: 15px;
    letter-spacing: 2px;
    fill: var(--strip-ink);
  }
  .subtitle {
    position: absolute;
    left: 0;
    top: 802px;
    width: 100%;
    text-align: center;
    font-family: "Arimo", Arial, sans-serif;
    font-size: 23px;
    line-height: 27px;
    color: var(--subtitle);
  }
</style>
</head>
<body>
  <main class="book-cover">
    <svg class="cover-art" width="592" height="948" viewBox="0 0 592 948" xmlns="http://www.w3.org/2000/svg">
      <defs>
        <radialGradient id="medallion-tone" cx="50%" cy="48%" r="55%">
          <stop offset="0" stop-color="var(--medallion-core)"/>
          <stop offset="0.6" stop-color="var(--medallion-mid)"/>
          <stop offset="1" stop-color="var(--medallion-edge)"/>
        </radialGradient>
        <linearGradient id="chest-tone" x1="0" y1="0" x2="0" y2="1">
          <stop offset="0" stop-color="var(--chest)"/>
          <stop offset="1" stop-color="var(--chest-dark)"/>
        </linearGradient>
      </defs>

      <!-- carved stone medallion -->
      <circle class="medallion" cx="296" cy="450" r="285" fill="url(#medallion-tone)"
              role="img" aria-label="Carved stone medallion with a triangle emblem"/>

      <!-- title -->
      <text class="title-word" x="20" y="112" font-size="104" textLength="552" lengthAdjust="spacingAndGlyphs">DRIFT</text>
      <text class="title-word" x="20" y="220" font-size="112" textLength="552" lengthAdjust="spacingAndGlyphs">WOOD</text>
      <rect x="285" y="150" width="24" height="54" rx="4" fill="var(--cover)"/>
      <text class="title-article" x="297" y="166" text-anchor="middle">T</text>
      <text class="title-article" x="297" y="182" text-anchor="middle">H</text>
      <text class="title-article" x="297" y="198" text-anchor="middle">E</text>

      <!-- open tool chest -->
      <rect class="tool-chest" x="180" y="610" width="238" height="180" fill="url(#chest-tone)"
            role="img" aria-label="Open red tool chest with a compass and tools rising out of it"/>

      <!-- word strips -->
      <g transform="translate(220 648) rotate(32)">
        <rect x="-68" y="-16" width="136" height="32" fill="var(--strip)"/>
        <text class="strip-label" x="0" y="6" text-anchor="middle">SUCCESS</text>
      </g>
      <g transform="translate(326 596) rotate(-82)">
        <rect x="-96" y="-16" width="192" height="32" fill="var(--strip)"/>
        <text class="strip-label" x="0" y="6" text-anchor="middle">MOTIVATION</text>
      </g>
      <g transform="translate(430 612) rotate(-38)">
        <rect x="-102" y="-16" width="204" height="32" fill="var(--strip)"/>
        <text class="strip-label" x="0" y="6" text-anchor="middle">INSPIRATION</text>
      </g>

      <!-- author -->
      <text class="author-name" x="20" y="928" font-size="46" textLength="552" lengthAdjust="spacingAndGlyphs">LORENZO VETTI</text>
    </svg>

    <p class="subtitle">How To Use The Philosophy Of<br>Quillarism In Your Everyday Life</p>
  </main>
</body>
</html>
```